Deal Email Template Design

I need a number of email templates designed for my deal website. The emails will be used to promote, market, and sell it's deals. Emails will be launched using an email marketing platform. I will work with chosen designer to detail the company description, branding, logos, etc.
Updates
Reason: I added details to project and would like to see some more bids. Please feel free to submit and ask any questions.
Thank you.
Target Market(s)
Casino Destination Travelers
Industry/Entity Type
It Company
Look and feel
Each slider illustrates characteristics of the customer's brand and the style your logo design should communicate.

```html
<!DOCTYPE html>
<html lang="en">
<head>
<meta charset="utf-8">
<title>Vexora casino deals – email</title>
<link rel="stylesheet" href="https://fonts.googleapis.com/css2?family=Arimo:wght@400;700&display=swap">
<style>
  :root{
    --black:#000000;
    --logo-panel:#1c1c1c;
    --icon-bar:#141414;
    --yellow:#fddf5f;
    --gold:#f6b31c;
    --button:#f7b21a;
    --cell-light:#f4f4f4;
    --cell-dark:#e9e9e9;
    --ink:#111111;
    --grey-text:#7d7d7d;
    --white:#ffffff;
    --accent-pink:#e2127f;
  }
  *{margin:0;padding:0;box-sizing:border-box}
  html,body{width:1200px;height:2852px;overflow:hidden;background:var(--white)}
  body{font-family:"Arimo",Arial,sans-serif;color:var(--ink);position:relative}

  .header{position:absolute;left:0;top:0;width:1200px;height:288px;background:var(--black)}
  .brand{position:absolute;left:248px;top:68px;width:692px;height:192px;background:var(--logo-panel);
    display:flex;flex-direction:column;align-items:center;justify-content:center}
  .brand-name{font-size:84px;font-weight:700;color:var(--gold);line-height:1}
  .brand-tag{font-size:36px;color:var(--white);margin-top:8px;line-height:1}

  .hero{position:absolute;left:0;top:288px;width:1200px;height:584px;background:var(--yellow)}
  .hero-title{position:absolute;left:552px;top:78px;font-size:68px;font-weight:700;line-height:1}
  .hero-copy{position:absolute;left:552px;top:160px;width:620px;font-size:33px;line-height:45px;white-space:nowrap}
  .hero-button{position:absolute;left:446px;top:432px;width:344px;height:60px;background:var(--button);
    color:var(--white);font-size:24px;font-weight:700;display:flex;align-items:center;justify-content:center}

  .grid{position:absolute;left:0;top:872px;width:1200px;display:grid;grid-template-columns:600px 600px}
  .cell{height:636px;position:relative;text-align:center}
  .cell.light{background:var(--cell-light)}
  .cell.dark{background:var(--cell-dark)}
  .grid .cell:nth-child(3),.grid .cell:nth-child(4){height:632px}
  .photo{border-radius:50%;box-shadow:0 10px 12px rgba(0,0,0,.18)}
  .cell .photo{position:absolute;left:172px;top:40px;width:256px;height:256px}
  .cell .promo-title{position:absolute;left:0;right:0;top:334px;font-size:27px;font-weight:700;line-height:36px}
  .cell .promo-copy{position:absolute;left:0;right:0;top:372px;font-size:29px;line-height:40px;color:var(--grey-text)}

  .feature{position:absolute;left:0;top:2140px;width:1200px;height:272px;background:var(--white)}
  .feature .photo{position:absolute;left:340px;top:16px;width:240px;height:240px}
  .feature .promo-title{position:absolute;left:616px;top:62px;font-size:27px;font-weight:700;line-height:36px}
  .feature .promo-copy{position:absolute;left:616px;top:100px;font-size:29px;line-height:40px;color:var(--grey-text)}

  .footer{position:absolute;left:0;top:2412px;width:1200px;height:316px;background:var(--black);text-align:center}
  .social{position:absolute;left:232px;top:8px;width:728px;height:140px;background:var(--icon-bar);
    display:flex;justify-content:space-around;align-items:center;padding:0 40px}
  .social span{width:44px;height:44px;border-radius:50%;background:var(--white)}
  .contact-email{position:absolute;left:0;right:0;top:160px;font-size:38px;font-weight:700;color:var(--gold);line-height:44px}
  .contact-web{position:absolute;left:0;right:0;top:214px;font-size:46px;font-weight:700;color:var(--white);line-height:54px}

  .label{position:absolute;left:14px;top:2750px;font-size:60px;font-weight:700;color:var(--accent-pink);line-height:1}
</style>
</head>
<body>
  <header class="header">
    <div class="brand">
      <span class="brand-name">Vexora</span>
      <span class="brand-tag">casino deals</span>
    </div>
  </header>

  <section class="hero">
    <h1 class="hero-title">Main promotion</h1>
    <p class="hero-copy">Lorem ipsum dolor sit amet, consectetur<br>adipiscing elit.Lorem ipsum dolor sit amet,<br>consectetur adipiscing elit.Lorem ipsum<br>dolor sit amet, consectetur adipiscing<br>elit.Lorem ipsum dolor sit amet,</p>
    <div class="hero-button">Click to continue</div>
  </section>

  <section class="grid">
    <article class="cell light">
      <div class="photo" role="img" aria-label="Las Vegas welcome sign" style="background:radial-gradient(circle at 50% 45%,#f2e9e4 0%,#d83a3a 45%,#1f3f8c 80%)"></div>
      <h2 class="promo-title">promotion</h2>
      <p class="promo-copy">Lorem ipsum dolor sit amet,<br>consectetur adipiscing elit.</p>
    </article>
    <article class="cell dark">
      <div class="photo" role="img" aria-label="Casino resort towers at night" style="background:linear-gradient(160deg,#4a2a8a 0%,#c4307a 50%,#2b1a4d 100%)"></div>
      <h2 class="promo-title">promotion</h2>
      <p class="promo-copy">Lorem ipsum dolor sit amet,<br>consectetur adipiscing elit.</p>
    </article>
    <article class="cell dark">
      <div class="photo" role="img" aria-label="Stacks of casino chips on a gaming table" style="background:radial-gradient(circle at 40% 40%,#e24848 0%,#7a4fb0 50%,#1d3f7a 100%)"></div>
      <h2 class="promo-title">promotion</h2>
      <p class="promo-copy">Lorem ipsum dolor sit amet,<br>consectetur adipiscing elit.</p>
    </article>
    <article class="cell light">
      <div class="photo" role="img" aria-label="Guests enjoying a night at the casino table" style="background:linear-gradient(150deg,#8a3a6a 0%,#d9a58a 50%,#3a2a3a 100%)"></div>
      <h2 class="promo-title">promotion</h2>
      <p class="promo-copy">Lorem ipsum dolor sit amet,<br>consectetur adipiscing elit.</p>
    </article>
  </section>

  <section class="feature">
    <div class="photo" role="img" aria-label="Neon-lit casino strip at night" style="background:linear-gradient(160deg,#3a2a7a 0%,#d2388a 55%,#2a1a3a 100%)"></div>
    <h2 class="promo-title">Promotion</h2>
    <p class="promo-copy">Lorem ipsum dolor sit amet,<br>consectetur adipiscing elit.</p>
  </section>

  <footer class="footer">
    <nav class="social" aria-label="Social links">
      <span></span><span></span><span></span><span></span><span></span>
    </nav>
    <p class="contact-email">info@vexora.com</p>
    <p class="contact-web">www.vexora.com</p>
  </footer>

  <p class="label">promotion</p>
</body>
</html>
```